redesing professional certificate

Redesign our certificate to more a professional look and to make it look like a-wanna have - Best in adobe photoshop, because this template will be our basic, and we have in our education different levels, basic, upper, lower, complex, master level. I usually add a small picture to show what level they are. Or when you have a better suggestion I a gladly to hear.
We teach to physiotherapist so it has to look professional.

Target Market(s)

physiotherapist

Industry/Entity Type

Health Care

Requirements
Must have
• our logo

```html
<!DOCTYPE html>
<html lang="en">
<head>
<meta charset="utf-8">
<title>Certificate – Tissue Balance Therapy</title>
<link href="https://fonts.googleapis.com/css2?family=Libre+Baskerville:wght@400;700&family=Merriweather:ital,wght@0,400;1,700&family=Source+Sans+3:wght@700&display=swap" rel="stylesheet">
<style>
  :root {
    --backdrop: #262628;
    --paper-edge: #e2e4e8;
    --gold: #fdd014;
    --gold-deep: #f2bd0c;
    --navy: #1f3a5c;
    --ink: #2d4868;
    --ribbon: #2d4d72;
    --ribbon-side: #21729f;
    --ribbon-fold: #4a2a1a;
    --steel-light: #f4f6f8;
    --steel-dark: #6f7478;
    --rim-blue: #2a5d92;
    --ornament: #3b76b0;
    --bronze: #b98a45;
  }
  html, body {
    margin: 0;
    width: 1200px;
    height: 945px;
    overflow: hidden;
    background: var(--backdrop);
  }
  .certificate {
    position: absolute;
    left: 20px;
    top: 62px;
    width: 1160px;
    height: 820px;
    display: block;
  }
  .heading { font-family: "Libre Baskerville", serif; font-size: 56px; fill: #f4f4f6; letter-spacing: 1px; }
  .lead { font-family: "Merriweather", serif; font-size: 16px; fill: var(--ink); letter-spacing: 0.5px; }
  .recipient { font-family: "Source Sans 3", sans-serif; font-weight: 700; font-size: 24px; fill: var(--navy); letter-spacing: 0.5px; }
  .course { font-family: "Merriweather", serif; font-style: italic; font-weight: 700; font-size: 16px; fill: var(--navy); }
  .body-text { font-family: "Merriweather", serif; font-size: 16.5px; fill: var(--ink); }
  .signatory { font-family: "Merriweather", serif; font-size: 16px; fill: var(--ink); }
  .tagline { font-family: "Libre Baskerville", serif; font-weight: 700; font-size: 19px; fill: var(--navy); letter-spacing: 4px; }
  .brand-name { font-family: "Source Sans 3", sans-serif; font-weight: 700; font-size: 58px; fill: #ffffff; }
</style>
</head>
<body>
<svg class="certificate" viewBox="0 0 1373 971" xmlns="http://www.w3.org/2000/svg">
  <defs>
    <radialGradient id="paper-fill" cx="50%" cy="50%" r="70%">
      <stop offset="0" stop-color="#ffffff"/>
      <stop offset="1" stop-color="#e2e4e8"/>
    </radialGradient>
    <linearGradient id="steel" x1="0" y1="0" x2="1" y2="0">
      <stop offset="0" stop-color="#6f7478"/>
      <stop offset="0.25" stop-color="#f4f6f8"/>
      <stop offset="0.5" stop-color="#9aa0a5"/>
      <stop offset="0.75" stop-color="#f4f6f8"/>
      <stop offset="1" stop-color="#6f7478"/>
    </linearGradient>
    <radialGradient id="gold-fill" cx="50%" cy="45%" r="60%">
      <stop offset="0" stop-color="#fdd014"/>
      <stop offset="1" stop-color="#f2bd0c"/>
    </radialGradient>
  </defs>

  <!-- sheet -->
  <rect class="sheet" width="1373" height="971" fill="url(#paper-fill)"/>
  <rect class="sheet-pattern" width="1373" height="971" fill="#dfe2e6" opacity="0.25" role="img" aria-label="Faint guilloche line pattern and floral border across the paper"/>

  <!-- frame: steel ring, blue rim, gold field -->
  <ellipse class="ring-steel" cx="688" cy="500" rx="648" ry="378" fill="url(#steel)"/>
  <ellipse class="ring-blue" cx="694" cy="503" rx="643" ry="354" fill="var(--rim-blue)"/>
  <ellipse class="field" cx="698" cy="503" rx="638" ry="349" fill="url(#gold-fill)"/>
  <ellipse class="field-pattern" cx="698" cy="503" rx="638" ry="349" fill="#f7c40e" opacity="0.25" role="img" aria-label="Fine guilloche pattern inside the gold field"/>

  <!-- faint ribbon tails -->
  <path class="ribbon-ghost" d="M170 415 L390 300 L400 360 L255 440 Z" fill="#d9a80a" opacity="0.45"/>
  <path class="ribbon-ghost" d="M1205 415 L985 300 L975 360 L1120 440 Z" fill="#d9a80a" opacity="0.45"/>

  <!-- ribbon banner -->
  <path class="ribbon-side" d="M353 270 L450 258 L460 340 L390 358 L378 343 Z" fill="var(--ribbon-side)"/>
  <path class="ribbon-side" d="M1021 270 L924 258 L914 340 L984 358 L996 343 Z" fill="var(--ribbon-side)"/>
  <path class="ribbon-fold" d="M378 343 L390 358 L400 336 Z" fill="var(--ribbon-fold)"/>
  <path class="ribbon-fold" d="M996 343 L984 358 L974 336 Z" fill="var(--ribbon-fold)"/>
  <path class="ribbon-main" d="M455 238 Q685 292 915 238 L940 315 Q685 375 433 315 Z" fill="var(--ribbon)"/>
  <text class="heading" x="686" y="320" text-anchor="middle" transform="rotate(-1 686 300)">CERTIFICATE</text>

  <!-- brand mark -->
  <circle class="brand-disc" cx="685" cy="141" r="94" fill="#ffffff"/>
  <circle class="brand-disc" cx="685" cy="141" r="89" fill="var(--navy)"/>
  <text class="brand-name" x="685" y="162" text-anchor="middle">TBT</text>

  <!-- body -->
  <text class="lead" x="687" y="384" text-anchor="middle">THIS CERTIFIES THAT</text>
  <text class="recipient" x="686" y="433" text-anchor="middle">LUCAS MORENO</text>
  <text class="course" x="681" y="467" text-anchor="middle">has completed the fasciatherapy level I course</text>
  <text class="course" x="681" y="493" text-anchor="middle">3 days, 75-77 february 2020</text>
  <text class="course" x="683" y="519" text-anchor="middle">Kópavogur, Iceland 77,  February 2020.</text>

  <line class="divider" x1="301" y1="542" x2="1063" y2="542" stroke="#fff3b0" stroke-width="1.2"/>
  <line class="divider" x1="301" y1="546" x2="1063" y2="546" stroke="#fff3b0" stroke-width="1.2"/>

  <text class="body-text" x="683" y="586" text-anchor="middle">The Tissue Balance Therapy ongoing certification is contingent upon meeting the</text>
  <text class="body-text" x="683" y="617" text-anchor="middle">requirements of the maintenance of the certification of Fasciatherapy</text>

  <!-- signatories -->
  <text class="signatory" x="259" y="690">Mr. JP van Dalen</text>
  <text class="signatory" x="259" y="712">Co-Director</text>
  <text class="signatory" x="1118" y="690" text-anchor="end">Mr. RT Halvors</text>
  <text class="signatory" x="1118" y="712" text-anchor="end">Co-Director</text>

  <ellipse class="ornament" cx="683" cy="693" rx="180" ry="12" fill="var(--ornament)" opacity="0.35" role="img" aria-label="Blue scroll flourish ornament"/>

  <!-- issuer -->
  <text class="signatory" x="683" y="754" text-anchor="middle">Fasciaplus BV, Tweede Lindengracht 14,</text>
  <text class="signatory" x="683" y="779" text-anchor="middle">1015KL Amsterdam,  The Netherlands</text>
  <text class="signatory" x="683" y="824" text-anchor="middle">Registration number: 4 KPV 21</text>

  <ellipse class="crest" cx="686" cy="864" rx="90" ry="18" fill="var(--bronze)" opacity="0.8" role="img" aria-label="Bronze crest with scroll ornament"/>

  <text class="tagline" x="686" y="931" text-anchor="middle">EXPERTS IN MANUAL TISSUE EDUCATION</text>
</svg>
</body>
</html>
```